Label or packaging Design for Hair Care Line

Dear Designer,
We are Corvella, a brand known for our premium hairstyling tools, and we are excited to expand into hair care. We are currently looking for a talented designer to create the label designs for our entire luxury hair care line.
This project is crucial in establishing our visual identity in the hair care market, and we aim to position ourselves alongside premium brands such as PLX, Varnette Coif Atelier, and Trevo.
Project Scope
We need a cohesive label design for our hair care line, which includes:
5 products (e.g., shampoo, conditioner, hair oil, styling cream, and a hair mask).
The designs should include:
Front label: Highlighting the product name, key features, and branding.
Our goal is to achieve a design that communicates premium luxury with a touch of professionalism. Below are the specific guidelines to help you align with our vision:
Style and Inspiration
Think of brands like PLX, Varnette Coif Atelier, and Trevo.
Luxury and Minimalism: Clean lines, sophisticated typography, and an elegant color palette.
Subtle femininity: premium finishes like metallic accents (gold, silver, or rose gold).
Brand Personality
Premium: Reflecting high quality and exclusivity.
Modern & Professional: Appealing to a refined, professional audience but also suitable for lifestyle-oriented customers.
Warm & Empowering: A brand that celebrates confidence and individuality.
Color Palette
Neutral tones like black, white, accented with metallics (gold or silver) for a luxurious feel.
Colors that feel timeless and elegant rather than trendy or overly bright.
Typography
Use clean, modern fonts (preferably sans-serif or serif for a refined look).
Clear and legible for all product details while maintaining a high-end aesthetic.
Materials and Finishes
Packaging Shape
The label designs should suit a variety of bottle and jar shapes (e.g., cylindrical, flat, or rounded).
Keep scalability in mind so the identity remains consistent across different products.
Deliverables
To understand the aesthetic we are aiming for, here are some brands to use as inspiration:
PLX: For its minimalistic and modern approach.
Varnette Coif Atelier: For its combination of luxury and professional appeal.
Trevo: For its soft femininity and lifestyle branding.
we would like to see your designs applied to a variety of packaging types to get an overall impression of how the brand identity works across different product formats. This includes:
A squeeze bottle (e.g., for styling creams or conditioners).
A glass bottle with a dropper (e.g., for a luxurious hair oil).
A shampoo/conditioner bottle (standard pump or flip-top cap).
A spray bottle (e.g., for leave-in treatments or heat protectors).
By creating designs for these different packaging types, we can better evaluate how cohesive and versatile the brand identity will be across the entire product line.

Updates
As you may have noticed from the designs, they don’t quite align with our briefing. The look needs to be clean and professional, similar to Varnette, PLX, and the other examples we provided. Please address this, and we’ll check it!

Target Market(s)
europe and us
Font styles to use
Other font styles liked:
- century gothic

Look and feel
Each slider illustrates characteristics of the customer's brand and the style your logo design should communicate.

```html
<!DOCTYPE html>
<html lang="en">
<head>
<meta charset="UTF-8">
<title>Corvella Hair Mask Label</title>
<link href="https://fonts.googleapis.com/css2?family=Outfit:wght@300;400;500&display=swap" rel="stylesheet">
<style>
  :root {
    --backdrop: #d9d9d9;
    --label-white: #f7f7f7;
    --label-shade: #e4e4e4;
    --ink: #1c1c1c;
    --ink-soft: #3a3a3a;
    --rose-gold: #c49a86;
    --rose-gold-light: #e6cfc4;
  }
  html, body {
    margin: 0;
    padding: 0;
    width: 1200px;
    height: 1200px;
    overflow: hidden;
    background: var(--backdrop);
    font-family: "Outfit", sans-serif;
  }
  .canvas {
    position: relative;
    width: 1200px;
    height: 1200px;
  }
  .label {
    position: absolute;
    left: 360px;
    top: 51px;
    width: 480px;
    height: 1097px;
    background: linear-gradient(90deg, var(--label-shade) 0%, var(--label-white) 22%, var(--label-white) 70%, var(--label-shade) 100%);
    color: var(--ink);
  }
  .brand-name {
    position: absolute;
    left: 50%;
    top: 250px;
    transform: translate(-50%, -50%) rotate(-90deg);
    font-weight: 300;
    font-size: 84px;
    letter-spacing: 0.02em;
    line-height: 1;
    white-space: nowrap;
    color: var(--ink);
  }
  .product-name {
    position: absolute;
    left: 0;
    right: 0;
    top: 668px;
    text-align: center;
    font-weight: 500;
    font-size: 24px;
    letter-spacing: 0.38em;
    padding-left: 0.38em;
    color: var(--ink-soft);
  }
  .ornament-area {
    position: absolute;
    left: 50%;
    top: 748px;
    width: 140px;
    height: 145px;
    transform: translateX(-50%);
    border-radius: 50%;
    background: radial-gradient(circle, var(--label-white) 30%, var(--rose-gold-light) 62%, var(--label-white) 78%);
  }
  .description {
    position: absolute;
    left: 0;
    right: 0;
    top: 929px;
    margin: 0 auto;
    width: 250px;
    text-align: center;
    font-weight: 300;
    font-size: 11.5px;
    line-height: 1.2;
    color: var(--ink-soft);
  }
  .volume {
    position: absolute;
    left: 0;
    right: 0;
    top: 1047px;
    text-align: center;
    font-weight: 300;
    font-size: 23px;
    color: var(--ink);
  }
</style>
</head>
<body>
  <main class="canvas">
    <section class="label">
      <div class="brand-name">Corvella</div>
      <div class="product-name">HAIR MASK</div>
      <div class="ornament-area" role="img" aria-label="Rose gold ornament of almond-shaped leaves arranged in a ring"></div>
      <p class="description">Lorem ipsum dolor sit amet, consectetur adipiscing elit, sed do eiusmod tempor incididunt ut labore et dolore magna aliqua Ut enim ad minim veniam, quis tui estre efit nostrud exercitation.</p>
      <div class="volume">100ml℮</div>
    </section>
  </main>
</body>
</html>
```